Lumavorne Business Card Design

I need a business card design for a new Business, that is focused on Custom Made Designer Furniture. that is aimed at the mid to high end markets. I would like a card that would in some way portray what I do for my clients in the way we are able to make any idea a reality and also work within a set budget to meet their requirements.
I like quite contemporary colours and styling and I want the final design to communicate a Contemporary and Professional image.

Target Market(s)

mid to high end market

Industry/Entity Type

Business

Contact Information for Business Card

Lumavorne
Harold Brenning
82 Wendle Ave, Tarrow, Auckland, New Zealand 0927.

Requirements
Nice to have
• I would also like to utilize the spot gloss or raised print on my cards

```html
<!DOCTYPE html>
<html lang="en">
<head>
<meta charset="UTF-8">
<title>Lumavorne Business Card</title>
<link href="https://fonts.googleapis.com/css2?family=Questrial&display=swap" rel="stylesheet">
<style>
  :root {
    --backdrop: #e9e6e2;
    --panel-brown: #3a302c;
    --panel-charcoal: #222222;
    --name-first: #1d4d4a;
    --name-last: #2b86b8;
    --brand-text: #cfcfcf;
    --tagline-text: #9a9a9a;
    --address-text: #7a3f8c;
    --trail-tone: #2e2b2a;
  }
  * { margin: 0; padding: 0; box-sizing: border-box; }
  html, body {
    width: 1200px;
    height: 741px;
    overflow: hidden;
    background: var(--backdrop);
  }
  .canvas {
    width: 1200px;
    height: 741px;
    display: flex;
    align-items: center;
    justify-content: center;
  }
  .business-card {
    position: relative;
    width: 980px;
    height: 560px;
    display: flex;
    font-family: "Questrial", sans-serif;
    box-shadow: 0 10px 30px rgba(0,0,0,0.25);
  }
  .name-panel {
    width: 40%;
    background: var(--panel-brown);
    padding: 54px 0 0 48px;
  }
  .holder-name {
    font-size: 50px;
    line-height: 1.05;
    font-weight: 400;
  }
  .holder-name .first { display: block; color: var(--name-first); }
  .holder-name .last { display: block; color: var(--name-last); padding-left: 24px; }
  .info-panel {
    position: relative;
    width: 60%;
    background: var(--panel-charcoal);
    text-align: right;
    padding: 64px 44px 0 0;
  }
  .brand-name {
    font-size: 42px;
    letter-spacing: 1px;
    color: var(--brand-text);
    line-height: 1;
  }
  .tagline {
    margin-top: 8px;
    font-size: 22px;
    font-style: italic;
    color: var(--tagline-text);
  }
  .address {
    margin-top: 110px;
    font-size: 22px;
    line-height: 1.5;
    color: var(--address-text);
  }
  .footprint-trail {
    position: absolute;
    left: 14px;
    bottom: 50px;
    width: 190px;
    height: 80px;
    border-radius: 6px;
    background: linear-gradient(100deg, var(--trail-tone), #262423);
  }
</style>
</head>
<body>
  <main class="canvas">
    <article class="business-card">
      <section class="name-panel">
        <h1 class="holder-name">
          <span class="first">Harold</span>
          <span class="last">Brenning</span>
        </h1>
      </section>
      <section class="info-panel">
        <h2 class="brand-name">LUMAVORNE</h2>
        <p class="tagline">Custom Made Designer Furniture</p>
        <p class="address">82 Wendle Ave, Tarrow<br>Auckland, New Zealand 0927</p>
        <div class="footprint-trail" role="img" aria-label="Faint trail of footprints walking across the card"></div>
      </section>
    </article>
  </main>
</body>
</html>
```